Educational non-profit needs an End of the Year Flyer

We need a flyer to mail to our supporters asking for donations to our program. Hillcrest Open Learning Hub runs after school programs for low-income students in Pasadena, CA. This is our end of the year mailing to supporters asking them to finish out the year with their contributions so that we can meet our budget.

Target Market(s)

Donors and supporters of organization

Industry/Entity Type

Non-Profit

Font styles to use
Serif

Colors

Designer to choose colors to be used in the design.

Requirements
Must have
• The project should fit on a 6x9" card, and be printed on front and back. It should show pictures, use the copy I have included, a space for a label address, a stamp, and the return address.
Nice to have
• eye-catching, fun

```html
<!DOCTYPE html>
<html lang="en">
<head>
<meta charset="utf-8">
<title>Hillcrest Open Learning Hub – End of Year Mailer</title>
<link href="https://fonts.googleapis.com/css2?family=Montserrat:wght@400;500;600;700&display=swap" rel="stylesheet">
<style>
  :root {
    --stage: #e6e6e6;
    --yellow: #f0e21b;
    --yellow-deep: #cfc000;
    --ink: #1b1b1b;
    --body: #3a3a3a;
    --link: #8a7b00;
    --paper: #ffffff;
    --back-frame: #e9e9e9;
    --rule: #8c8c8c;
    --box-line: #d9d9d9;
    --stamp: #e2e2e2;
  }
  * { box-sizing: border-box; margin: 0; padding: 0; }
  html, body { width: 1200px; height: 860px; overflow: hidden; background: var(--stage); }
  body { position: relative; font-family: "Montserrat", sans-serif; color: var(--ink); }

  .card {
    position: absolute; top: 164px;
    width: 675px; height: 952px;
    transform: scale(0.6); transform-origin: top left;
    overflow: hidden; background: var(--paper);
  }
  .card--front { left: 177px; }
  .card--back { left: 644px; background: var(--back-frame); }

  .card__art { position: absolute; inset: 0; width: 675px; height: 952px; }

  .brand-mark {
    position: absolute; left: 440px; top: 40px; width: 230px;
    display: flex; flex-direction: column; align-items: center; gap: 10px;
    text-align: center;
  }
  .brand-mark__dot { width: 34px; height: 34px; border-radius: 50%; background: var(--yellow); border: 3px solid var(--ink); }
  .brand-mark__name { font-size: 19px; font-weight: 700; line-height: 1.2; color: var(--ink); }

  .appeal__title {
    position: absolute; left: 0; top: 560px; width: 675px;
    text-align: center; font-size: 20px; font-weight: 600; line-height: 26px; letter-spacing: 0.3px;
  }
  .appeal__box {
    position: absolute; left: 58px; top: 624px; width: 554px; height: 193px;
    border: 1.5px solid #d6cf8a; border-radius: 22px; background: var(--paper);
    box-shadow: 0 4px 8px rgba(0,0,0,0.15);
    padding: 20px 30px 0; text-align: center;
  }
  .appeal__copy { font-size: 12.4px; line-height: 16px; color: var(--body); }
  .appeal__copy strong { color: var(--ink); }
  .appeal__cta { margin-top: 14px; font-size: 13.4px; font-weight: 600; line-height: 18px; }
  .appeal__cta a { color: var(--link); text-decoration: none; }

  .site-line {
    position: absolute; left: 50px; top: 898px;
    display: flex; align-items: center; gap: 8px;
    font-size: 24px; font-weight: 600; color: var(--ink);
  }

  .back__panel {
    position: absolute; left: 32px; top: 33px; width: 611px; height: 886px;
    background: var(--paper); border: 2px solid var(--rule);
  }
  .address-box {
    position: absolute; width: 283px; height: 128px;
    border: 1.5px solid var(--box-line); border-radius: 22px; background: var(--paper);
    display: flex; flex-direction: column; justify-content: center; align-items: center;
    font-size: 14px; font-weight: 600; line-height: 18px; text-align: center;
  }
  .address-box--return { left: 59px; top: 75px; }
  .address-box--label { left: 318px; top: 745px; }
  .stamp { position: absolute; left: 558px; top: 104px; width: 56px; height: 68px; background: var(--stamp); }

  .back__brand {
    position: absolute; left: 187px; top: 290px; width: 300px;
    display: flex; flex-direction: column; align-items: center; gap: 12px; text-align: center;
  }
  .back__brand .brand-mark__dot { width: 44px; height: 44px; }
  .back__brand .brand-mark__name { font-size: 24px; }

  .contact {
    position: absolute; left: 0; top: 461px; width: 675px; text-align: center;
    font-size: 17px; font-weight: 600; line-height: 21.5px;
  }
  .contact__phone { margin-top: 6px; font-size: 46px; font-weight: 700; line-height: 54px; letter-spacing: 0.5px; }

  .back__photo {
    position: absolute; left: 0; top: 577px; width: 292px; height: 375px;
    background: radial-gradient(ellipse at 50% 60%, #8d8d8d 0%, #b9b9b9 45%, rgba(240,240,240,0) 80%);
  }
</style>
</head>
<body>

<section class="card card--front" aria-label="Flyer front">
  <svg class="card__art" viewBox="0 0 675 952">
    <defs>
      <linearGradient id="crowd" x1="0" y1="0" x2="1" y2="1">
        <stop offset="0" stop-color="#c9c3b4"/>
        <stop offset="0.45" stop-color="#6b4a3e"/>
        <stop offset="1" stop-color="#3b2a28"/>
      </linearGradient>
      <linearGradient id="band" x1="0" y1="0" x2="1" y2="0">
        <stop offset="0" stop-color="#c9bb00"/>
        <stop offset="0.5" stop-color="#f2e41c"/>
        <stop offset="1" stop-color="#fff58a"/>
      </linearGradient>
      <linearGradient id="swing" x1="0" y1="0" x2="1" y2="1">
        <stop offset="0" stop-color="#ffffff" stop-opacity="0"/>
        <stop offset="0.4" stop-color="#b38d86"/>
        <stop offset="1" stop-color="#4b3a44"/>
      </linearGradient>
    </defs>

    <rect x="0" y="0" width="675" height="560" fill="url(#crowd)" role="img" aria-label="Photo of a large group of students celebrating together in a restaurant"/>

    <path d="M360 0 C372 130 520 205 675 200 L675 222 C505 228 350 140 340 0 Z" fill="var(--yellow)"/>
    <path d="M360 0 C372 130 520 205 675 200 L675 0 Z" fill="var(--paper)" stroke="var(--ink)" stroke-width="7"/>

    <path d="M0 470 C170 395 430 380 675 560 L675 600 C430 430 170 440 0 510 Z" fill="var(--yellow)"/>
    <path d="M0 495 C170 420 430 405 675 580" fill="none" stroke="var(--ink)" stroke-width="10"/>
    <path d="M0 512 C170 440 430 428 675 600 L675 952 L0 952 Z" fill="var(--paper)"/>

    <circle cx="162" cy="432" r="96" fill="var(--yellow)"/>
    <circle cx="162" cy="432" r="86" fill="#7d6a78" role="img" aria-label="Photo of students posing in a gym"/>
    <circle cx="382" cy="445" r="80" fill="var(--yellow)"/>
    <circle cx="382" cy="445" r="71" fill="#a57a55" role="img" aria-label="Photo of students playing guitars on stage"/>
    <circle cx="560" cy="512" r="64" fill="var(--ink)"/>
    <circle cx="560" cy="512" r="57" fill="#8d6a64" role="img" aria-label="Photo of children preparing food"/>

    <rect x="405" y="767" width="270" height="185" fill="url(#swing)" role="img" aria-label="Photo of girls sitting together on a swing"/>

    <path d="M0 872 C210 850 390 862 520 952 L0 952 Z" fill="url(#band)"/>
    <path d="M0 858 C210 834 400 846 540 952" fill="none" stroke="var(--ink)" stroke-width="14"/>
  </svg>

  <div class="brand-mark">
    <span class="brand-mark__dot"></span>
    <span class="brand-mark__name">Hillcrest Open<br>Learning Hub</span>
  </div>

  <h1 class="appeal__title">WILL YOU JOIN WITH US FOR<br>AN END OF THE YEAR CONTRIBUTION?</h1>

  <div class="appeal__box">
    <p class="appeal__copy">We need your help to finish out 2018 strong! We have had a wonderful 25th year of serving the children and families of Pasadena here at Hillcrest Open Learning Hub with high quality afterschool programs. Hundreds and hundreds of students have been a part of the Bright Start Kids Club family. Our annual budget is <strong>$275,000</strong> and we count on <strong>$100,000</strong> from individual donors. Will you join with us for an end of the year contribution? Remember, you can give online through GiveSecure.</p>
    <p class="appeal__cta">Just look for the link on our website - <a href="#">www.hillcrest-hub.org.</a><br>Merry Christmas from all of us at HOLH!</p>
  </div>

  <div class="site-line">
    <svg width="26" height="26" viewBox="0 0 26 26" aria-hidden="true">
      <g fill="none" stroke="var(--ink)" stroke-width="1.8">
        <circle cx="13" cy="13" r="11"/>
        <ellipse cx="13" cy="13" rx="5" ry="11"/>
        <line x1="2" y1="13" x2="24" y2="13"/>
        <line x1="4" y1="7.5" x2="22" y2="7.5"/>
        <line x1="4" y1="18.5" x2="22" y2="18.5"/>
      </g>
    </svg>
    <span>www.hillcrest-hub.org</span>
  </div>
</section>

<section class="card card--back" aria-label="Flyer back">
  <div class="back__panel"></div>

  <div class="address-box address-box--return">
    <span>Hillcrest Open Learning Hub</span>
    <span>412 N. Alder Ave.</span>
    <span>Pasadena, CA&nbsp; 91104</span>
  </div>
  <div class="stamp" aria-label="Stamp area"></div>

  <div class="back__brand">
    <span class="brand-mark__dot"></span>
    <span class="brand-mark__name">Hillcrest Open<br>Learning Hub</span>
  </div>

  <div class="contact">
    <p>Website - www.hillcrest-hub.org</p>
    <p>FriendSpace - Hillcrest Open Learning Hub</p>
    <p>Email:&nbsp; hello@hillcrest-hub.org</p>
    <p class="contact__phone">(626) 555-0148</p>
  </div>

  <div class="back__photo" role="img" aria-label="Photo of a smiling student holding a handwritten thank-you letter"></div>

  <div class="address-box address-box--label">
    <span>Hillcrest Open Learning Hub</span>
    <span>412 N. Alder Ave.</span>
    <span>Pasadena, CA&nbsp; 91104</span>
  </div>
</section>

</body>
</html>
```